Bold Creative Business Card for Digital Marketing Company (Contest)

NOTICE TO DESIGNERS: We understand this is how you make your living. Our commitment to you is to give you awesome and rapid feedback. If we don't think you are on the right track or have a chance of winning we will let you know right away so you don't have to focus your time with us and can continue to get work.

We respect the crowdsource community greatly. We have launched hundreds of crowdsource projects and will make this a great experience for you if you choose to participate (we hope you will!)

--------------
Brief
-------------

We are a cutting edge digital marketing company and we need a new, bold and creative business card designed to reflect who we are and what we do. We want our brand to stand out and be noticed.

The name of our company is: Tundrel Web Marketing

Definition of Tundrel:

a. a person pursuing rebellious, even potentially disruptive, policies or ideas:

b. a lone dissenter, as an intellectual, an artist, or a politician, who takes an independent stand apart from his or her associates

c. unorthodox, unconventional, nonconformist

Our businesses is helping small to medium size businesses with their online marketing using bold and creative outside the box strategies that get results.

We are an industry leader and need our business cards to stand out when we hand them out to people, and to be amazing so we stand out and "lead the pack"!

Our current website: http://www.tundrelwebmarketing.example

We are rebranding our site to reflect the new logo we just got but you will at least have an idea of who we are and what we do.

Colors We Want: We would like to see burnt Orange, Dark Blue, Gray and/or Black.

We need a front and back designed!

Be creative! Even to the point of creative-shaped business cards. Think outside the box. Let nothing stop your imagination! At the very least, we know that we want business cards that are not the US Standard 2"x3.5"... but rather the wider 3.35"x2.17" (European Standard) with rounded corners if you want to stick with a rectangular shape.

On the front we need:

Our Logo
Place for a name ie Dale Voskuij
Place for our phone number (505) 555 - 7680
Place for email name@tundrelwebmarketing.example
Place for our website www.TundrelWebMarketing.example

Optional... Place for a headshot photo of the person who the business card will be used for

On the back we need:

The wording... FREE VIDEO SERIES! "9 Quick Moves To Grow Your Company This Week!" www.TundrelWebMarketing.example/SmartIdeas

We are excited to see what you come up with.

Thank you for your interests and for participating in this contest!
Updates

Hi everyone! Thanks for all your submissions. However, we feel that most of you are "missing" what we're looking for. Almost all of the designs that have come in are what we would call "standard", "generic", or "typical". We are looking for something creative, different, attention-getting, a business card that would stand out amongst a stack of other business cards. I've shot this video: http://clipvault.example/t/qPzTbw4hYcs Please take the time to review it. Let us know if you have questions. Thanks!

Target Market(s)

Our target market is small to medium sized business owners who need help with their online marketing.

Industry/Entity Type

Marketing

Font styles to use
Sans Serif

Colors
0355a3
85acd3
f78f20
f37022
faa54b
f68d4d

Requirements
Must have
• On the front we need:

Our Logo

Be CREATIVE! INTERESTING!

On the back we need:

Use the colors from our logo!
Nice to have
• Optional... Place for a headshot photo of the person who the business card will be used for.
Should not have
• Boring, "traditional" look and feel. We want and need to stand out!

```html
<!DOCTYPE html>
<html lang="en">
<head>
<meta charset="utf-8">
<title>Tundrel Web Marketing – Business Card</title>
<link rel="stylesheet" href="https://fonts.googleapis.com/css2?family=Gelasio:wght@400;700&display=swap">
<style>
  :root {
    --page: #ffffff;
    --card-dark: #0a0a0b;
    --card-light: #ffffff;
    --card-edge: #b9b9b9;
    --ink: #111111;
    --ink-inverse: #ffffff;
    --brand-blue: #0355a3;
    --brand-orange: #f37022;
    --brand-amber: #faa54b;
    --photo-light: #9fb3cc;
    --photo-dark: #2c3f5a;
    --shadow: rgba(0, 0, 0, 0.55);
  }
  * { margin: 0; padding: 0; box-sizing: border-box; }
  html, body {
    width: 1200px; height: 1000px; overflow: hidden;
    background: var(--page);
    font-family: "Gelasio", Georgia, serif;
    color: var(--ink);
  }
  .canvas { position: relative; width: 1200px; height: 1000px; }

  .card {
    position: absolute; left: 278px; width: 643px; height: 367px;
    border-radius: 20px;
    box-shadow: -4px 6px 8px var(--shadow);
  }
  .card--front { top: 123px; background: var(--card-dark); }
  .card--back { top: 510px; background: var(--card-light); border: 1px solid var(--card-edge); }

  /* front */
  .brand-lockup {
    position: absolute; left: 0; right: 0; top: 190px;
    display: flex; align-items: center; justify-content: center; gap: 14px;
  }
  .brand-mark { width: 26px; height: 26px; background: var(--brand-orange); }
  .brand-name {
    font-size: 40px; font-weight: 700; letter-spacing: 1px;
    color: var(--ink-inverse); line-height: 1;
  }
  .front-url {
    position: absolute; left: 0; right: 0; top: 324px;
    text-align: center; font-size: 19px; color: var(--ink-inverse);
  }

  /* back */
  .back-brand {
    position: absolute; right: 18px; top: 62px;
    display: flex; align-items: center; gap: 8px;
  }
  .back-brand .brand-mark { width: 14px; height: 14px; }
  .back-brand .brand-name { font-size: 19px; color: var(--ink); letter-spacing: 0.5px; }

  .headshot {
    position: absolute; left: 19px; top: 125px;
    width: 116px; height: 116px; border-radius: 50%;
    border: 3px solid var(--brand-orange);
    padding: 4px; background: var(--card-light);
  }
  .headshot__fill {
    width: 100%; height: 100%; border-radius: 50%;
    background: radial-gradient(circle at 50% 40%, var(--photo-light), var(--photo-dark));
  }

  .contact { position: absolute; left: 152px; top: 168px; }
  .contact__name { font-size: 19px; font-weight: 400; margin-bottom: 14px; }
  .contact__name strong { font-weight: 700; }
  .contact__line { font-size: 17px; line-height: 20px; }

  .divider {
    position: absolute; left: 20px; top: 270px; width: 603px; height: 2px;
    background: var(--brand-blue);
  }
  .promo { position: absolute; left: 17px; top: 282px; font-size: 17px; line-height: 23px; }
  .promo__title { font-weight: 700; }
</style>
</head>
<body>
<main class="canvas">
  <section class="card card--front" aria-label="Card front">
    <div class="brand-lockup">
      <span class="brand-mark" aria-hidden="true"></span>
      <span class="brand-name">Tundrel Web Marketing</span>
    </div>
    <p class="front-url">www.tundrelwebmarketing.example</p>
  </section>

  <section class="card card--back" aria-label="Card back">
    <div class="back-brand">
      <span class="brand-mark" aria-hidden="true"></span>
      <span class="brand-name">Tundrel Web Marketing</span>
    </div>

    <div class="headshot">
      <div class="headshot__fill" role="img" aria-label="Headshot photo of the card holder"></div>
    </div>

    <div class="contact">
      <p class="contact__name">Dale <strong>Voskuij</strong></p>
      <p class="contact__line">(505) 555 - 7680</p>
      <p class="contact__line">dale@tundrelwebmarketing.example</p>
    </div>

    <div class="divider" aria-hidden="true"></div>

    <div class="promo">
      <p class="promo__title">FREE VIDEO SERIES!</p>
      <p>"9 Quick Moves To Grow Your Company This Week!"</p>
      <p>www.TundrelWebMarketing.example/SmartIdeas</p>
    </div>
  </section>
</main>
</body>
</html>
```